Financial Sevices firm looking for Brochure design

Our company Veltmoor Capital and Holdings Limited (VeltHoldings)
i
Is an investment/advisory firm - www.veltholdings-grp.net
We invest in the energy sector in Africa and offer advisory services to Energy companies looking to invest in Africa. From oil and gas, to renewables (wind/solar). We are more focused on the "West African" Sub region
We need corporate brochure (Booklet style) to circulate to our corporate clients
We would like to see a design that considers the colours in our Logo (see website)
HI Guys, sorry been travelling. Seen some very good submissions and will be sending updates shortly
Reason: Dear Designers,
Thank you for participating in this project and for some of the great designs i've received so far. Unfortunately, due to the holidays, it has been difficult to consult with other members of my team. As a result, the project deadline is extended by about 12 days
I appreciate your understanding in the situation and looking forward to continuing the excellent collaboration in the coming days
Reason: Hi All,
Apologies for the multiple deadline extensions and thanks so much for all the designs which my team and I will be reviewing today and tomorrow.
We will be closing this project tomorrow by 6pm GMT (17th Jan 2014)
Thanks to all those that submitted such wonderful designs and goodluck!!
Project to be closed finally on 17th Jan 2014 at 6pm GMT
Banks, Investment Firms, Energy companies, Private Equity Funds
I have attached a Brochure that I created myself as an example of the type of information required but please also feel free to visit our website www.veltholdings-grp.net
Looking for any creative ideas you have to suplement the information provided.
Financial

```html
<!DOCTYPE html>
<html lang="en">
<head>
<meta charset="utf-8">
<title>VeltHoldings Brochure Spread</title>
<link href="https://fonts.googleapis.com/css2?family=Open+Sans:wght@300;600&family=Roboto:wght@300;400&family=Roboto+Condensed:ital,wght@1,700&display=swap" rel="stylesheet">
<style>
  :root {
    --red: #f20d00;
    --red-deep: #c40a00;
    --black: #161616;
    --charcoal: #474c4d;
    --quote-grey: #4a4f50;
    --white: #ffffff;
    --paper: #ffffff;
    --bg: #ffffff;
    --mist: #f4f6f6;
  }
  * { margin: 0; padding: 0; box-sizing: border-box; }
  html, body { width: 1200px; height: 1000px; overflow: hidden; background: var(--bg); }
  body { position: relative; font-family: "Roboto", Arial, sans-serif; }

  .page {
    position: absolute; top: 123px; width: 532px; height: 754px;
    background: var(--paper); overflow: hidden;
    box-shadow: 2px 4px 10px rgba(0,0,0,0.35);
  }
  .page--left { left: 56px; }
  .page--right { left: 613px; }
  .block { position: absolute; }

  /* Left page */
  .strengths {
    left: 28px; top: 55px; width: 442px; height: 165px;
    background: var(--red); color: var(--white);
    padding: 14px 4px 0 32px; font-size: 13.6px; line-height: 21px; font-weight: 300;
  }
  .strengths li { list-style: none; position: relative; }
  .strengths li::before {
    content: ""; position: absolute; left: -20px; top: 5px;
    width: 9px; height: 9px; border-radius: 50%;
    background: var(--white); border: 2px solid #777;
  }
  .strengths li + li { margin-top: 10px; padding-top: 9px; border-top: 1px dotted rgba(255,255,255,0.8); }
  .strengths li + li::before { top: 14px; }

  .tagline-bar {
    left: 28px; top: 220px; width: 442px; height: 43px;
    background: var(--black); color: var(--white);
    font-family: "Open Sans", Arial, sans-serif;
    font-weight: 300; font-size: 23px; line-height: 43px; padding-left: 28px;
  }
  .motto {
    left: 62px; top: 300px; width: 400px; height: 130px;
    font-family: "Roboto Condensed", "Arial Narrow", sans-serif; font-style: italic; font-weight: 700;
    color: var(--red); font-size: 42px; line-height: 40px; letter-spacing: -1px;
  }
  .motto .quote { color: var(--quote-grey); font-size: 70px; vertical-align: -10px; }
  .motto .line2 { display: block; padding-left: 48px; }
  .motto .amp { font-family: "Open Sans", sans-serif; font-style: normal; font-weight: 300; font-size: 50px; letter-spacing: -3px; }

  .finance-visual {
    left: 0; top: 420px; width: 532px; height: 308px;
    background: radial-gradient(ellipse 60% 55% at 55% 60%, #a4a4a4 0%, #c9c9c9 45%, #efefef 80%, #ffffff 100%);
  }
  .foot-band-red { left: 0; top: 728px; width: 471px; height: 26px; background: var(--red); }
  .foot-band-grey { left: 471px; top: 728px; width: 61px; height: 26px; background: var(--charcoal); }

  /* Right page */
  .brand {
    left: 45px; top: 60px; display: flex; align-items: center; gap: 6px;
    font-family: "Open Sans", Arial, sans-serif;
    font-size: 21px; font-weight: 600; color: var(--red); letter-spacing: -0.5px;
  }
  .brand-mark { width: 18px; height: 18px; background: var(--red); }

  .tile { position: absolute; }
  .tile--power { left: 45px; top: 107px; width: 230px; height: 105px; background: linear-gradient(180deg, #e23a00, #ff9a3c); }
  .tile--rig { left: 45px; top: 215px; width: 114px; height: 94px; background: linear-gradient(180deg, #d9e6ea, #6f8f9a 60%, #b3271c); }
  .tile--wind { left: 162px; top: 215px; width: 113px; height: 74px; background: linear-gradient(180deg, #6fb0da, #8fc3a0 70%, #5f7d55); }
  .tile--red-a { left: 279px; top: 149px; width: 107px; height: 140px; background: var(--red); }
  .tile--mist { left: 391px; top: 187px; width: 86px; height: 64px; background: var(--mist); }
  .tile--grey { left: 391px; top: 255px; width: 108px; height: 114px; background: var(--charcoal); }
  .tile--red-b { left: 45px; top: 313px; width: 114px; height: 56px; background: var(--red); }
  .tile--pipes { left: 162px; top: 293px; width: 140px; height: 76px; background: linear-gradient(160deg, #8a8a8a, #d7a53a 55%, #6e4a2a); }
  .tile--team { left: 306px; top: 293px; width: 79px; height: 76px; background: radial-gradient(circle at 50% 50%, #b99a86, #e8ecef 75%); }

  .dark-section {
    left: 0; top: 389px; width: 532px; height: 365px;
    background: radial-gradient(ellipse 80% 60% at 60% 20%, #5a0c08 0%, #2a0806 55%, #140505 100%);
  }
  .about {
    left: 45px; top: 444px; width: 454px; height: 253px;
    background: rgba(226, 12, 4, 0.92); color: var(--white);
    padding: 17px 20px 0 22px; font-size: 13.8px; line-height: 20.8px; font-weight: 300;
    text-align: justify;
  }
  .about p + p { margin-top: 12px; padding-top: 10px; border-top: 1px solid rgba(255,255,255,0.35); }
</style>
</head>
<body>

<section class="page page--left">
  <ul class="block strengths">
    <li>Unique ability to deliver tailor-made solutions including structuring project and operating capital, project budget analysis, modeling, securing attractively-priced capital.</li>
    <li>Collective experience in originating, appraising, structuring, and financing investments in infrastructure assets worth over US$ 10 billion across Africa.</li>
  </ul>
  <div class="block tagline-bar">Our Triple Bottom Line is</div>
  <div class="block motto"><span class="quote">“</span>People<span class="line2">Profit<span class="amp">&amp;</span>Planet<span class="quote">”</span></span></div>
  <div class="block finance-visual" role="img" aria-label="Grey 3D illustration of a globe, rising bar chart with arrow and currency symbols on a world map"></div>
  <div class="block foot-band-red"></div>
  <div class="block foot-band-grey"></div>
</section>

<section class="page page--right">
  <div class="block brand"><span class="brand-mark"></span>VeltHoldings</div>

  <div class="tile tile--power" role="img" aria-label="Photo of electricity pylons against an orange sky"></div>
  <div class="tile tile--rig" role="img" aria-label="Photo of an offshore oil platform vessel"></div>
  <div class="tile tile--wind" role="img" aria-label="Photo of wind turbines on a coastline"></div>
  <div class="tile tile--red-a"></div>
  <div class="tile tile--mist"></div>
  <div class="tile tile--grey"></div>
  <div class="tile tile--red-b"></div>
  <div class="tile tile--pipes" role="img" aria-label="Photo of industrial gas pipelines"></div>
  <div class="tile tile--team" role="img" aria-label="Photo of business team hands stacked together"></div>

  <div class="block dark-section" role="img" aria-label="Dark red abstract light streak background"></div>
  <div class="block about">
    <p>We are dedicated to promoting the sustainable implementation of infrastructure and energy related projects in Africa through direct investments and by facilitating private and institutional investments. Our narrow sector focus enables us to provide in-depth services and insightful investment solutions.</p>
    <p>Our team brings a wealth of international expertise in the areas of transaction structuring, public-private partnerships (PPP), financial and economic modeling, legal and regulatory reform, and operations.</p>
  </div>
</section>

</body>
</html>
```